Etiketten für Gin
Zielgruppe
Foodtruck & Catering - Philosophie FRISCH / REGIONAL / AUTHENTISCH
Zielgruppe 20-45 Jahre mit einem Bewusstsein für frische & gesunde Ernährung, Flair für Genusszeit & Zeit mit Freunden.
Weitere Informationen: www.lekrawatt.ch
Aufgabenstellung
Etikett bzw. Direkt-Aufdruck (Siebdruck) für GIN-Flasche
Anhand des beiliegenden Dossier 'Le Krawatt Gin Etikette' können wir folgende Informationen & Wünsche geben:
- Siebdruck weiss einfarbig direkt auf schwarze Flasche
- Vektorisierte, gepfadete Datei PDF, EPS etc
- Strichstärke mind. 0.15mm
- Datei als Negativ (was gedruckt wird in Schwarz), Druckfarbe PANTONE
Zwingende Angaben: «Dry Gin» / «41%Vol» / «50cl» / «Hergestellt von: Velbrand Brennerei GmbH CH-8000 Zürich»
Zutatenverzeichnis ist nach Art. 16 Abs. 4 der VERORDNUNG EU Nr. 1169/2011 nicht erfoderlich
Vorne: Illustrativ Stil wie auf der Seite 2 & 3 (Owl at Dusk, Bacon, Skizze 'Le Krawatt Gin')
Text «Krawatt Dry Gin» (ohne 'Le'), 41%Vol 50cl, evt. «Solothurn»
Illustration mit krawatt (mit oder ohne Béret) sowie Bezug zum Produkt (siehe unten)
Hinten: Unser Logo, «Le Krawatt GmbH» evt. «Solothurn», «Hergestellt von …», Kleiner Text zu Unternehmen & Produkt (s. unten), Referenz zum Designer (wenn du möchtest)
Den Text liefern wir in der nötigen Kürze/Länge, oder du zauberst etwas ???? Der Gin ist sommerlich-frisch und hebt sich ab durch Noten von Yuzu, Minze & Süssholz. Pur, eiskalt, als Gin & Tonic (mit Zitronenscheibe) oder in Kombination mit der Krawatt Limo, perfekter Apéro-Begleiter.
ACHTUNG: Auf der Rückseite der schwarzen GIN-Flasche ist ein eingestanzter/eingebrannter Marker '0.5l M.K.M' (siehe Druckvorlage). Dieser darf/soll nicht überschrieben werden. Entsprechend könnte wenn nötig die Mengenangabe auf der Vorderseite (50cl) entfallen.
FOLGEAUFTRAG möglich
Wir sind in der Zielgerade für unsere eigene Limo & Eistee. Bei Interesse & Zufriedenheit würden wir diesen Auftrag gerne demselben Team/GrafikerIn übergeben wie die Gin-Flasche.

```html
<!DOCTYPE html>
<html lang="de">
<head>
<meta charset="utf-8">
<title>Krawatt Dry Gin – Etikette</title>
<link href="https://fonts.googleapis.com/css2?family=Delius&family=Caveat:wght@500&family=Barlow+Condensed:wght@500;600&display=swap" rel="stylesheet">
<style>
  :root {
    --paper: #f5f5f5;
    --ink: #1c1c1c;
    --glass: #0b0b0b;
    --print: #ffffff;
    --print-soft: #e8e8e8;
    --illu-light: #d9d9d9;
    --illu-dark: #3a3a3a;
  }
  * { margin: 0; padding: 0; box-sizing: border-box; }
  html, body { width: 1200px; height: 2258px; overflow: hidden; background: var(--paper); }
  .canvas { position: relative; width: 1200px; height: 2258px; }

  .label { position: absolute; text-align: center; color: var(--ink); }
  .brand { font-family: "Delius", cursive; letter-spacing: 1px; line-height: 1; }
  .product { font-family: "Delius", cursive; line-height: 1; letter-spacing: 4px; }
  .origin { font-family: "Caveat", cursive; font-weight: 500; line-height: 1; }
  .volume { font-family: "Barlow Condensed", sans-serif; font-weight: 600; line-height: 1; letter-spacing: -0.5px; }
  .mustache { display: block; margin: 0 auto; border-radius: 50% 50% 45% 45% / 30% 30% 70% 70%; }

  /* master artwork */
  .master { left: 0; top: 180px; width: 1200px; }
  .master .brand { font-size: 96px; margin-left: 50px; }
  .master .product { font-size: 138px; margin-top: 26px; }
  .master .mustache { width: 622px; height: 210px; margin-top: 60px;
    background: linear-gradient(180deg, var(--illu-light), #bdbdbd); }
  .master .origin { font-size: 88px; margin-top: 38px; }
  .master .volume { font-size: 58px; margin-top: 42px; }

  /* print previews: white screen print on black glass */
  .print-panel { position: absolute; top: 1208px; width: 416px; height: 1000px; background: var(--glass); border-radius: 70px 70px 30px 30px; }
  .print-panel.front { left: 136px; }
  .print-panel.back { left: 653px; }
  .print-panel .label { color: var(--print); left: 0; width: 100%; }

  .front .label { top: 460px; }
  .front .brand { font-size: 56px; margin-left: 36px; }
  .front .product { font-size: 82px; margin-top: 6px; letter-spacing: 2px; }
  .front .mustache { width: 340px; height: 118px; margin-top: 28px;
    background: linear-gradient(180deg, var(--illu-dark), #1e1e1e); }
  .front .origin { font-size: 54px; margin-top: 24px; }
  .front .volume { font-size: 33px; margin-top: 20px; }

  .back .label { top: 474px; }
  .back .house { display: flex; align-items: center; justify-content: center; gap: 10px; font-family: "Delius", cursive; font-size: 20px; line-height: 1; }
  .back .house .dot { width: 16px; height: 16px; border-radius: 50%; background: var(--print); }
  .back .brand { font-size: 30px; margin-top: 26px; margin-left: 20px; }
  .back .product { font-size: 38px; letter-spacing: 1px; margin-top: 2px; }
  .back .story { font-family: "Delius", cursive; font-size: 15.5px; line-height: 1.18; margin-top: 24px; color: var(--print-soft); }
  .back .story p + p { margin-top: 17px; }
  .back .maker { position: absolute; left: 0; width: 100%; top: 932px; font-family: "Barlow Condensed", sans-serif; font-weight: 500; font-size: 13px; color: var(--print); text-align: center; transform: rotate(-1.5deg); }
</style>
</head>
<body>
<main class="canvas">

  <section class="label master">
    <div class="brand">krawatt</div>
    <div class="product">DRY GIN</div>
    <div class="mustache" role="img" aria-label="Linienillustration eines geschwungenen Schnurrbarts"></div>
    <div class="origin">Solothurn</div>
    <div class="volume">41%Vol . 50cl</div>
  </section>

  <section class="print-panel front" aria-label="Vorderseite Siebdruck">
    <div class="label">
      <div class="brand">krawatt</div>
      <div class="product">DRY GIN</div>
      <div class="mustache" role="img" aria-label="Schnurrbart-Illustration in Weiss"></div>
      <div class="origin">Solothurn</div>
      <div class="volume">41%Vol . 50cl</div>
    </div>
  </section>

  <section class="print-panel back" aria-label="Rückseite Siebdruck">
    <div class="label">
      <div class="house"><span class="dot"></span>Le Krawatt</div>
      <div class="brand">krawatt</div>
      <div class="product">DRY GIN</div>
      <div class="story">
        <p>Wir lieben es frisch, regional und authentisch.</p>
        <p>Unser sommerlich-frischer Gin besticht<br>mit Noten von Yuzu, Minze &amp; Süssholz.</p>
        <p>Genieße ihn pur, eiskalt, als Gin &amp; Tonic,<br>als Kombi mit Krawatt Limo<br>oder als perfekter Apéro-Begleiter.</p>
      </div>
    </div>
    <div class="maker">Hergestellt von Velbrand Brennerei GmbH CH-8000 Zürich</div>
  </section>

</main>
</body>
</html>
```